need Window envelope designs 110mm x 220mm

Lumaro Events host events / outings for all over the world. colour should be around the same with the logo . Need fresh and professional feeling. best it have some light waves making sure the envelope dun look empty or messy.

                                        kindly send up designs with window too . thanks!

```html
<!DOCTYPE html>
<html lang="en">
<head>
<meta charset="utf-8">
<title>Lumaro Events – DL Window Envelope Set</title>
<link rel="preconnect" href="https://fonts.googleapis.com">
<link href="https://fonts.googleapis.com/css2?family=Cinzel:wght@600&display=swap" rel="stylesheet">
<style>
  :root {
    --backdrop: #ebebeb;
    --paper: #f7f7f7;
    --paper-edge: #dcdcdc;
    --flap-shade: #efefef;
    --window-fill: #fbfcfd;
    --window-edge: #cfd5d9;
    --brand-blue: #2b7fa8;
    --brand-deep: #123f5a;
    --brand-light: #5fb3d6;
    --silver: #c9cdd0;
    --silver-dark: #8f969b;
  }
  * { margin: 0; padding: 0; box-sizing: border-box; }
  html, body {
    width: 1200px;
    height: 795px;
    overflow: hidden;
    background: var(--backdrop);
  }
  .stationery-set {
    position: relative;
    width: 1200px;
    height: 795px;
  }
  .envelope {
    position: absolute;
    width: 520px;
    height: 260px;
    background: var(--paper);
    border: 1px solid var(--paper-edge);
    box-shadow: 0 10px 24px rgba(0, 0, 0, 0.12);
    overflow: hidden;
  }
  .envelope--back { left: 50px; top: 267px; }
  .envelope--front { left: 630px; top: 267px; }

  .envelope__flap {
    position: absolute;
    left: 0;
    top: 0;
    width: 100%;
    height: 100%;
  }
  .flap-brand {
    position: absolute;
    left: 50%;
    top: 34px;
    transform: translateX(-50%);
    display: flex;
    align-items: center;
    gap: 8px;
    font-family: "Cinzel", serif;
    font-weight: 600;
    font-size: 13px;
    letter-spacing: 0.08em;
    color: var(--brand-blue);
    white-space: nowrap;
  }
  .flap-brand__dot {
    width: 12px;
    height: 12px;
    border-radius: 50%;
    background: var(--brand-blue);
  }

  .address-window {
    position: absolute;
    left: 262px;
    top: 46px;
    width: 226px;
    height: 84px;
    border: 1px solid var(--window-edge);
    border-radius: 6px;
    background: var(--window-fill);
    box-shadow: inset 0 1px 3px rgba(0, 0, 0, 0.05);
  }

  .brand-name {
    position: absolute;
    left: 30px;
    top: 150px;
    font-family: "Cinzel", serif;
    font-weight: 600;
    font-size: 17px;
    letter-spacing: 0.06em;
    color: var(--brand-blue);
    white-space: nowrap;
  }

  .wave-graphic {
    position: absolute;
    right: 0;
    bottom: 0;
    width: 320px;
    height: 110px;
  }
</style>
</head>
<body>
  <main class="stationery-set">

    <section class="envelope envelope--back" aria-label="Envelope back with flap">
      <svg class="envelope__flap" viewBox="0 0 520 260" aria-hidden="true">
        <path d="M0 0 H520 V88 Q520 96 512 96 H20 Q0 96 0 80 Z" fill="var(--flap-shade)" stroke="var(--paper-edge)" stroke-width="1"/>
      </svg>
      <div class="flap-brand">
        <span class="flap-brand__dot"></span>
        <span>Lumaro Events</span>
      </div>
    </section>

    <section class="envelope envelope--front" aria-label="Envelope front with address window">
      <div class="address-window" aria-label="Address window"></div>
      <p class="brand-name">Lumaro Events</p>
      <svg class="wave-graphic" viewBox="0 0 320 110" preserveAspectRatio="none" role="img" aria-label="Decorative blue and silver light waves in the corner">
        <defs>
          <linearGradient id="wave-blue" x1="0" y1="0" x2="1" y2="1">
            <stop offset="0" stop-color="var(--brand-light)"/>
            <stop offset="0.6" stop-color="var(--brand-blue)"/>
            <stop offset="1" stop-color="var(--brand-deep)"/>
          </linearGradient>
          <linearGradient id="wave-silver" x1="0" y1="0" x2="1" y2="1">
            <stop offset="0" stop-color="#ffffff"/>
            <stop offset="0.5" stop-color="var(--silver)"/>
            <stop offset="1" stop-color="var(--silver-dark)"/>
          </linearGradient>
        </defs>
        <path d="M10 110 C70 90 110 40 180 26 C230 16 280 20 320 10 V110 Z" fill="url(#wave-silver)"/>
        <path d="M45 110 C100 96 140 62 200 50 C250 40 290 44 320 38 V110 Z" fill="url(#wave-blue)"/>
      </svg>
    </section>

  </main>
</body>
</html>
```